Etiquetas para platos preparados de la marca El Fogón Verde

Necesito el diseño de una belly band o etiquetas para productos cocinados. En ella debe aparecer la siguiente información: el logo de la marca,
Símbolos con la siguiente info: refrigerado entre 2º-4º, pincha el plástico que lo cubre, imagen microondas 3:00, disfruta.
Además necesito que la etiqueta tenga en la parte frontal una zona donde podamos modificar e ir añadiendo el nombre del producto en concreto y en la parte trasera una zona destinada también a los valores nutricionales personalizable.
Por último necesitamos que las etiquetas estén diseñadas en 6 colores diferentes para poder diferenciar entre diferentes categorías (ensaladas, carnes, pescados, postres, ECO...).
Los tamaños de los envases sobre los que debe ir el belly band es el siguiente:
-Formato 1: 180x180x35mm
-Formato 2: 168x128x35mm
-Formato 3: belly band de 30cm de largo

Target Market(s)

Producto expuesto es vitrinas expositoras de supermercados

Industry/Entity Type

Alimentación

Font styles to use
Sans Serif
Other font styles liked:
• Cocomat y Poppins

Requirements
Must have
• Atractivo visualmente. Fuentes empleadas Cocomat y Montserrat
Nice to have
• Los colores para diferenciar categorías y espacio para poder incluir nosotros el nombre de cada producto. Además un espacio que ponga Origen personalizable también y un logo que ponga casero 100%

```html
<!DOCTYPE html>
<html lang="es">
<head>
<meta charset="utf-8">
<title>El Fogón Verde – Belly bands</title>
<link rel="stylesheet" href="https://fonts.googleapis.com/css2?family=Montserrat:wght@300;400;500&family=Pathway+Gothic+One&display=swap">
<style>
  :root{
    --bg:#ededed;
    --white:#ffffff;
    --panel:#30434a;
    --panel-art:#3a4e55;
    --panel-art-end:#435860;
    --badge:#1ea812;
    --cat-ensaladas:#22cc0a;
    --cat-pescados:#d9aa1a;
  }
  *{margin:0;padding:0;box-sizing:border-box}
  html,body{width:1200px;height:958px;overflow:hidden;background:var(--bg)}
  .canvas{position:relative;width:1200px;height:958px}
  .band{position:absolute;top:29.5px;width:210px;height:901px;color:var(--white)}
  .band--ensaladas{left:20.6px;--accent:var(--cat-ensaladas)}
  .band--pescados{left:247.6px;top:30px;--accent:var(--cat-pescados)}
  .band__bg{position:absolute;inset:0;width:100%;height:100%;display:block}
  .band__bg .accent{fill:var(--accent)}
  .band__bg .wave{fill:var(--white)}
  .panel{position:absolute;left:18.4px;top:205.5px;width:175px;height:500px;background:var(--panel);border-radius:24px;overflow:hidden}
  .frame{position:absolute;left:21px;top:20px;width:137px;height:62px;
    border:1.6px solid var(--white);border-bottom:none;border-radius:12px 12px 0 0}
  .frame::after{content:"";position:absolute;right:-1.6px;top:30px;width:2px;height:32px;background:var(--panel)}
  .badge{position:absolute;left:108px;top:53px;width:59px;height:59px;border-radius:50%;
    background:var(--badge);border:2.5px solid var(--white)}
  .brand{position:absolute;left:0;width:175px;top:168px;text-align:center;
    font-family:"Montserrat",sans-serif;font-weight:300;font-size:15px;line-height:20px;letter-spacing:.3px;
    color:var(--white);text-transform:uppercase;white-space:nowrap}
  .category{position:absolute;left:0;width:175px;top:200px;text-align:center;
    font-family:"Pathway Gothic One",sans-serif;font-weight:400;font-size:44px;line-height:44px;
    color:var(--accent);transform:scaleY(1.3);transform-origin:top center;white-space:nowrap}
  .art{position:absolute;left:8px;width:159px;border-radius:14px;
    background:linear-gradient(180deg,var(--panel-art),var(--panel-art-end))}
  .band--ensaladas .art{top:272px;height:178px}
  .band--pescados .art{top:306px;height:144px}
  .info{position:absolute;left:8px;top:456px;width:161px;display:flex;justify-content:space-between;align-items:center;
    font-family:"Montserrat",sans-serif;color:var(--white)}
  .info__item{display:flex;align-items:center;gap:4px}
  .info__item svg{display:block;flex:none}
  .info__text{font-size:6.4px;line-height:8px;white-space:nowrap}
  .info__text .big{font-size:9px;line-height:10px;display:block}
</style>
</head>
<body>
<main class="canvas">

  <section class="band band--ensaladas" aria-label="Belly band Ensaladas">
    <svg class="band__bg" viewBox="0 0 378 1620" preserveAspectRatio="none" aria-hidden="true">
      <rect class="accent" width="378" height="1620"/>
      <path class="wave" d="M378,90 C350,200 300,200 220,270 C140,340 120,460 0,478 L0,1300 L378,1300 L378,1190 L378,440 C320,400 320,260 378,200 Z"/>
    </svg>
    <div class="panel">
      <div class="frame"></div>
      <div class="badge" role="img" aria-label="Sello natural"></div>
      <div class="brand">El Fogón Verde</div>
      <h2 class="category">ENSALADAS</h2>
      <div class="art" role="img" aria-label="Ilustración de verduras dibujadas a línea"></div>
      <div class="info">
        <div class="info__item">
          <svg width="12" height="26" viewBox="0 0 12 26"><path d="M4 2h4v15a5 5 0 1 1-4 0z" fill="none" stroke="#fff" stroke-width="1.6"/><circle cx="6" cy="20.5" r="2.2" fill="#fff"/></svg>
          <span class="info__text"><span class="big">2º-4º</span>Refrigerado Entre</span>
        </div>
        <div class="info__item">
          <svg width="28" height="20" viewBox="0 0 28 20"><rect x="1" y="2" width="26" height="15" rx="1.5" fill="none" stroke="#fff" stroke-width="1.2"/><rect x="3" y="4" width="17" height="11" fill="none" stroke="#fff" stroke-width=".8"/><text x="11.5" y="12.5" font-size="6" fill="#fff" text-anchor="middle" font-family="Montserrat,sans-serif">3:00</text><circle cx="23.5" cy="6" r="1" fill="#fff"/><circle cx="23.5" cy="9.5" r="1" fill="#fff"/><circle cx="23.5" cy="13" r="1" fill="#fff"/></svg>
          <span class="info__text">Imagen<br>Microondas</span>
        </div>
      </div>
    </div>
  </section>

  <section class="band band--pescados" aria-label="Belly band Pescados">
    <svg class="band__bg" viewBox="0 0 378 1620" preserveAspectRatio="none" aria-hidden="true">
      <rect class="accent" width="378" height="1620"/>
      <path class="wave" d="M378,90 C350,200 300,200 220,270 C140,340 120,460 0,478 L0,810 C20,830 30,860 40,880 L40,1300 L378,1300 L378,1190 L378,440 C320,400 320,260 378,200 Z"/>
    </svg>
    <div class="panel">
      <div class="frame"></div>
      <div class="badge" role="img" aria-label="Sello natural"></div>
      <div class="brand">El Fogón Verde</div>
      <h2 class="category">PESCADOS</h2>
      <div class="art" role="img" aria-label="Ilustración de un pescado dibujado a línea"></div>
      <div class="info">
        <div class="info__item">
          <svg width="12" height="26" viewBox="0 0 12 26"><path d="M4 2h4v15a5 5 0 1 1-4 0z" fill="none" stroke="#fff" stroke-width="1.6"/><circle cx="6" cy="20.5" r="2.2" fill="#fff"/></svg>
          <span class="info__text"><span class="big">2º-4º</span>Refrigerado Entre</span>
        </div>
        <div class="info__item">
          <svg width="28" height="20" viewBox="0 0 28 20"><rect x="1" y="2" width="26" height="15" rx="1.5" fill="none" stroke="#fff" stroke-width="1.2"/><rect x="3" y="4" width="17" height="11" fill="none" stroke="#fff" stroke-width=".8"/><text x="11.5" y="12.5" font-size="6" fill="#fff" text-anchor="middle" font-family="Montserrat,sans-serif">3:00</text><circle cx="23.5" cy="6" r="1" fill="#fff"/><circle cx="23.5" cy="9.5" r="1" fill="#fff"/><circle cx="23.5" cy="13" r="1" fill="#fff"/></svg>
          <span class="info__text">Imagen<br>Microondas</span>
        </div>
      </div>
    </div>
  </section>

</main>
</body>
</html>
```